An international wholesale business needs letterhead design

Logo file is attached. Please design a letterhead with the following details:

- Company Name and Logo
- Address
- VAT Registration number
- Phone No
- Website address

```html
<!DOCTYPE html>
<html lang="en">
<head>
<meta charset="utf-8">
<title>Corvela Trading Letterhead</title>
<link rel="stylesheet" href="https://fonts.googleapis.com/css2?family=Open+Sans:wght@400;600;700&display=swap">
<style>
  :root {
    --backdrop: #e9e6e1;
    --paper: #ffffff;
    --paper-top: #f1f1f1;
    --ink: #2b2b2b;
    --brand-red: #c8323a;
    --signature-tone: #dcdcdc;
  }
  * { box-sizing: border-box; margin: 0; padding: 0; }
  html, body {
    width: 1200px; height: 960px; overflow: hidden;
    background: var(--backdrop);
    font-family: "Open Sans", Arial, sans-serif;
    color: var(--ink);
  }
  .letterhead {
    position: absolute; left: 260px; top: 0;
    width: 679px; height: 960px;
    background: linear-gradient(180deg, var(--paper-top) 0%, var(--paper) 30%);
    box-shadow: 0 4px 18px rgba(0,0,0,.18);
    padding: 80px 80px 0 90px;
  }
  .brand { display: flex; align-items: center; gap: 12px; }
  .brand-dot {
    width: 34px; height: 34px; border-radius: 50%;
    background: var(--brand-red);
  }
  .brand-name {
    font-size: 26px; font-weight: 700; letter-spacing: 2px;
    color: var(--brand-red);
  }
  .recipient { margin-top: 110px; font-size: 13px; line-height: 20px; }
  .recipient .to { font-weight: 600; }
  .recipient .line { font-weight: 700; padding-left: 18px; }
  .body { margin-top: 20px; padding-left: 36px; font-size: 12px; line-height: 20px; }
  .body p + p { margin-top: 18px; }
  .closing { margin-top: 28px; padding-left: 110px; font-size: 12.5px; line-height: 20px; }
  .signature {
    width: 130px; height: 46px; margin: 6px 0 6px 10px;
    background: var(--signature-tone); border-radius: 4px;
  }
  .address {
    position: absolute; right: 40px; bottom: 62px;
    font-size: 10.5px; color: var(--ink);
  }
  .address .bar { color: var(--brand-red); margin-right: 8px; }
  .contact-row {
    position: absolute; left: 180px; right: 40px; bottom: 28px;
    display: flex; align-items: center; gap: 26px;
    font-size: 10px; color: var(--ink);
  }
  .contact-item { display: flex; align-items: center; gap: 5px; }
  .vat-label { color: var(--brand-red); }
  .contact-item svg { width: 11px; height: 11px; }
</style>
</head>
<body>
  <main class="letterhead">
    <header class="brand">
      <span class="brand-dot"></span>
      <span class="brand-name">CORVELA TRADING</span>
    </header>

    <section class="recipient">
      <div class="to">To</div>
      <div class="line">Lorem Ipsum is simply</div>
      <div class="line">Lorem Ipsum is Lorem Ipsum is</div>
      <div class="line">Lorem Ipsum is</div>
    </section>

    <section class="body">
      <p>dummy text of the printing and typesetting industry. Lorem Ipsum has been the industry's standard dummy text ever since the 1500s, when an unknown printer took a galley of type and scrambled it to make a type specimen book. It has survived not only five centuries, but also the leap into electronic typesetting, remaining essentially unchanged.</p>
      <p>It is a long established fact that a reader will be distracted by the readable content of a page when looking at its layout. The point of using Lorem Ipsum is that it has a more-or-less normal distribution of letters, as opposed to using 'Content here, content here', making it look like readable English. Many desktop publishing packages and web page editors now use Lorem Ipsum as their default model text, and a search for 'lorem .</p>
      <p>Contrary to popular belief, Lorem Ipsum is not simply random text. It has roots in a piece of classical Latin literature from 45 BC, making it over 2000 years old. Martin Elsworth, a Latin professor at Brindlemoor College in Vermont, looked up one of the more obscure Latin words, consectetur, from a Lorem Ipsum passage,</p>
    </section>

    <section class="closing">
      <div>Lorem Ipsum</div>
      <div class="signature" role="img" aria-label="Handwritten signature"></div>
      <div>Lorem Ipsum is a dummy</div>
    </section>

    <div class="address"><span class="bar">|</span>Brunnweg 14, Address Line, STATE-30412</div>

    <footer class="contact-row">
      <span class="contact-item"><span class="vat-label">VAT</span> 47BC00981BC</span>
      <span class="contact-item">
        <svg viewBox="0 0 12 12"><circle cx="6" cy="6" r="6" fill="#c8323a"/><path d="M4 3.2l1 1.6-.6.6c.4.9 1 1.5 1.9 1.9l.6-.6 1.6 1-.5 1c-2.4-.3-4.2-2.1-4.5-4.5z" fill="#fff"/></svg>
        044 987 65 43
      </span>
      <span class="contact-item">
        <svg viewBox="0 0 12 12"><circle cx="6" cy="6" r="5.3" fill="none" stroke="#c8323a" stroke-width="1.2"/><path d="M1 6h10M6 1c-2 2.7-2 7.3 0 10M6 1c2 2.7 2 7.3 0 10" fill="none" stroke="#c8323a" stroke-width=".8"/></svg>
        corvelatrading.com
      </span>
    </footer>
  </main>
</body>
</html>
```